pharmacy/travel clinic business card design

We need a business card for our new business called Brenwick Travel Clinic and Pharmacy. Our primary focus is doing consultations for people before travelling internationally and providing vaccinations and prescriptions for them. While the business is considered a pharmacy, it has more the look and feel of a doctor's office. The design should communicate a professional and trustworthy feel. I have attached a copy of the logo we are going to be using.
Updates
Thanks for the submissions.  If you haven`t been eliminated you are one of the finalists.  Decision will likely be made tomorrow.

Target Market(s)
Customers, other health care professionals, travel agents
Industry/Entity Type
Clinic
Look and feel
Each slider illustrates characteristics of the customer's brand and the style your logo design should communicate.

```html
<!DOCTYPE html>
<html lang="en">
<head>
<meta charset="utf-8">
<title>Brenwick Travel Clinic and Pharmacy — Business Card</title>
<link rel="stylesheet" href="https://fonts.googleapis.com/css2?family=Questrial&display=swap">
<style>
  :root {
    --card-bg: #ffffff;
    --brand-green: #8dc63f;
    --brand-blue: #1b75bc;
    --accent-blue: #29a9e0;
    --soft-blue: #93d3ef;
    --soft-green: #c5e29a;
    --text-grey: #4d4d4d;
    --font-main: "Questrial", "Century Gothic", sans-serif;
  }
  html, body {
    margin: 0;
    padding: 0;
    width: 1200px;
    height: 734px;
    overflow: hidden;
    background: var(--card-bg);
  }
  .business-card {
    position: relative;
    width: 1200px;
    height: 734px;
    background: var(--card-bg);
    font-family: var(--font-main);
    overflow: hidden;
  }
  .accent-area {
    position: absolute;
    left: 587px;
    top: 0;
    width: 613px;
    height: 734px;
  }
  .brand {
    position: absolute;
    left: 58px;
    top: 100px;
    display: flex;
    align-items: flex-start;
    gap: 24px;
  }
  .brand-dot {
    width: 62px;
    height: 62px;
    margin-top: 16px;
    border-radius: 50%;
    background: var(--accent-blue);
    flex: none;
  }
  .brand-name {
    margin: 0;
    font-weight: 400;
    font-size: 64px;
    line-height: 1.08;
    color: var(--brand-green);
    letter-spacing: -0.5px;
    width: 640px;
  }
  .contact {
    position: absolute;
    left: 119px;
    top: 397px;
    margin: 0;
    font-style: normal;
    font-size: 30px;
    line-height: 39px;
    color: var(--text-grey);
  }
  .contact span { display: block; }
  .website {
    position: absolute;
    left: 119px;
    top: 636px;
    margin: 0;
    font-size: 30px;
    line-height: 39px;
    color: var(--brand-blue);
  }
</style>
</head>
<body>
  <main class="business-card">
    <svg class="accent-area" viewBox="0 0 613 734" role="img" aria-label="Large decorative brand accent in light blue and green">
      <defs>
        <radialGradient id="accent-blue-glow" cx="62%" cy="40%" r="60%">
          <stop offset="0" stop-color="var(--soft-blue)" stop-opacity="0.75"/>
          <stop offset="1" stop-color="var(--soft-blue)" stop-opacity="0"/>
        </radialGradient>
        <radialGradient id="accent-green-glow" cx="78%" cy="82%" r="45%">
          <stop offset="0" stop-color="var(--soft-green)" stop-opacity="0.8"/>
          <stop offset="1" stop-color="var(--soft-green)" stop-opacity="0"/>
        </radialGradient>
      </defs>
      <rect width="613" height="734" fill="url(#accent-blue-glow)"/>
      <rect width="613" height="734" fill="url(#accent-green-glow)"/>
    </svg>

    <header class="brand">
      <span class="brand-dot" aria-hidden="true"></span>
      <h1 class="brand-name">Brenwick Travel Clinic and Pharmacy</h1>
    </header>

    <address class="contact">
      <span class="contact-line">12345 Address, Suite</span>
      <span class="contact-line">County, City, State</span>
      <span class="contact-line">tel: 1 (555) 019-2846</span>
      <span class="contact-line">fax: 1 (555) 019-2847</span>
      <span class="contact-line">email: service@brenwicktravelclinic.com</span>
    </address>

    <p class="website">www.brenwicktravelclinic.com</p>
  </main>
</body>
</html>
```